Single Page Corporate Profile Web-site Design

We're a new IT Resourcing company called vanq5, and we need a ew single page corporate web-site to establish our credentials.

Our model is to extend IT resourcing to offer access to global resources, end to end management, and a structured approach resourcing process.

Phase 2 (out of scope) will be a full site build in approximately a month's time.

This project is to:
- Establish a look and feel for web, consistent with existing design work (logo an corporate presentation)
- Build the web pages
- Upload onto our domain hosting site (4&4)

The web-site:
We want a modern, clean and bold design.

We'd like a design that is consistent with our corporate presentation (sourceless supplied). In terms of look and feel and use of graphics.

KEY FEATURES
- Single page design.
- Navigation bar (to page sections) at the top of the page.
- No cookies (phase 1 design)
- Good example of preferred web page design:
www.plomtak42.com
https://brivo.com/regulator/days-with-brivo-regulator/
http://www.ombrelfinsystems.com
- Clear sections on page as structured in the attached slides.
- We would like some of the page sections to use imagery of your choice - but please no cliched "IT people" or "data-centre" images.
- Image use must be royalty free.

ANY ADVICE WELCOME ! It's been a while since we've done this.

Target Market(s)

Companies - mid-size, technically sophisticated IT developers.
Potential employees

Industry/Entity Type

It Company

Number of Pages Required

1 page

Font styles to use
Other font styles liked:
• calibri

Requirements
Must have
• Do's
• - Please use graphics and "look and feel" provided
• - Follow similar style of those sites provided
• - Take the provided content and develop it for the web
• - Page must load quickly (if you think there's too much on the page - say so, and we'll put it across a few"
• - Please use background imagery for some of the sections
Should not have
• Don'ts
• - Please don't use cliched imagery e.g. "IT people" or "data-centre lights"
• - Use dark colours

```html
<!DOCTYPE html>
<html lang="en">
<head>
<meta charset="utf-8">
<title>vanq5 – IT resourcing</title>
<link href="https://fonts.googleapis.com/css2?family=Roboto:wght@300;400;500;700&display=swap" rel="stylesheet">
<style>
:root{
  --orange:#f08a1c;
  --orange-cell:#f4a14a;
  --blue:#1ea7e1;
  --blue-dark:#1587c4;
  --navy:#1c2633;
  --navy-2:#2a3644;
  --ink:#2b2b2b;
  --grey-text:#555;
  --grey-bg:#eeeeee;
  --white:#ffffff;
}
*{box-sizing:border-box;margin:0;padding:0}
html,body{width:686px;height:1200px;overflow:hidden;background:var(--white)}
body{font-family:'Roboto',Arial,sans-serif;color:var(--ink);position:relative}

/* header */
.site-header{height:66px;display:flex;align-items:center;justify-content:space-between;padding:0 38px 0 52px}
.brand{display:flex;flex-direction:column;line-height:1}
.brand-name{font-size:30px;font-weight:700;color:var(--blue-dark);letter-spacing:-.5px}
.brand-tag{font-size:11px;font-weight:700;color:var(--blue-dark);margin-top:2px}
.main-nav{display:flex;gap:18px;font-size:8.5px;color:#777;margin-top:-10px}
.main-nav a{color:inherit;text-decoration:none;padding-bottom:4px}
.main-nav a.is-active{color:var(--orange);border-bottom:1px solid var(--orange)}

.hero{height:229px;background:linear-gradient(120deg,#3a3f48 0%,#9aa3ad 22%,#eef1f4 45%,#d7e6f2 70%,#f3f3f3 100%)}

/* about */
.about{height:147px;padding:12px 58px 0;text-align:center;font-size:7px;line-height:1.55;color:var(--grey-text)}
.section-title{font-weight:700;color:var(--navy-2)}
.about .section-title{font-size:16px;margin-bottom:7px;color:#1d3550}
.about .section-title span{color:var(--orange)}
.about p{margin-bottom:7px}
.about strong{color:var(--ink)}

/* approach */
.approach{height:402px;background:radial-gradient(circle at 80% 60%,#34414f 0%,var(--navy) 70%);position:relative;color:var(--white)}
.approach-head{text-align:center;padding-top:26px}
.approach-head h2{font-size:23px;font-weight:400;letter-spacing:.3px}
.divider{display:flex;align-items:center;justify-content:center;gap:4px;margin:8px 0 9px}
.divider i{width:56px;height:1px;background:rgba(255,255,255,.35)}
.divider b{width:8px;height:8px;border-radius:50%;background:var(--blue);box-shadow:0 0 0 2px rgba(30,167,225,.35)}
.approach-head p{font-size:7px;color:#d5d9de}
.device{position:absolute;left:60px;top:118px;width:255px;height:232px;border-radius:6px;background:linear-gradient(160deg,#e8eaee 0%,#9aa6b4 40%,#2f3b4a 100%)}
.benefits{position:absolute;left:352px;top:130px;width:290px;list-style:none}
.benefit{display:flex;gap:14px;margin-bottom:23px}
.benefit-icon{flex:0 0 34px;height:34px;border-radius:50%;background:var(--blue);display:flex;align-items:center;justify-content:center}
.benefit h3{font-size:9px;font-weight:500;color:var(--orange);margin:3px 0 4px}
.benefit p{font-size:7px;line-height:1.55;color:#d5d9de}

/* services */
.services{height:356px;text-align:center;padding-top:14px}
.services h2{font-size:22px;color:#222}
.services .divider i{background:#ccc}
.services .divider b{width:6px;height:6px;box-shadow:none}
.services-lead{font-size:7px;color:var(--grey-text)}
.service-grid{position:absolute;left:45px;top:944px;width:556px;height:236px;background:var(--grey-bg);text-align:left}
.badge{position:absolute;left:6px;width:103px;background:var(--blue);border-radius:6px;color:var(--white);font-weight:700;padding:6px 9px;line-height:1.1}
.badge .b-name{font-size:13px;display:block}
.badge .b-role{font-size:10px}
.col-type{position:absolute;left:129px;width:94px;background:var(--blue);border-bottom:1px solid var(--white);display:flex;align-items:center;justify-content:space-around;color:var(--white);font-size:8.5px;font-weight:700}
.col-detail{position:absolute;left:224px;width:330px;background:var(--orange-cell);border-bottom:1px solid var(--white);color:var(--white);font-size:10px;line-height:1.3;padding:4px 6px}
.col-detail ul{padding-left:20px}
.dotline{position:absolute;left:119px;border-left:1px dotted #999}
</style>
</head>
<body>
<header class="site-header">
  <div class="brand"><span class="brand-name">vanq5</span><span class="brand-tag">IT resourcing</span></div>
  <nav class="main-nav">
    <a class="is-active" href="#home">Home</a><a href="#about">About Us</a><a href="#services">Services</a><a href="#dna">Our DNA</a><a href="#competencies">Competencies</a><a href="#delivery">Delivery</a><a href="#contact">Contact</a>
  </nav>
</header>

<div class="hero" role="img" aria-label="Photo of business people's hands at a desk over printed bar charts and a pen"></div>

<section class="about" id="about">
  <h2 class="section-title">ABOUT <span>US</span></h2>
  <p>We created vanq5 because we wanted to offer something different in IT resourcing. We're expert at what we do, with a track record of IT Service Delivery and Resourcing excellence in high growth environments.</p>
  <p><strong>Martin Hale</strong> – With a background in sales management and recruitment, Martin founded a highly successful recruitment agency and built it into one of the UK's leading specialist agencies. Successfully exiting the businesses after 10 years.</p>
  <p><strong>Oliver Brandt</strong> – With a history in telecoms and IT services, Oliver has held many senior level positions from marketing to operations. His last role was as COO for an IT services company, supporting the growth from 250 to 2000 people whilst he was there. One of our core aims with vanq5 is to build a fantastic team. Happy team, happy customers, successful business!</p>
</section>

<section class="approach" id="dna">
  <div class="approach-head">
    <h2>AN ITERATION OF TRADITIONAL RESOURCING</h2>
    <div class="divider"><i></i><b></b><i></i></div>
    <p>In a market where outstanding people are hard to find, we wanted to offer a solution:</p>
  </div>
  <div class="device" role="img" aria-label="Illustration of a desktop monitor and a smartphone showing the website"></div>
  <ul class="benefits">
    <li class="benefit">
      <span class="benefit-icon"><svg width="20" height="20" viewBox="0 0 20 20"><circle cx="10" cy="10" r="8" fill="none" stroke="#fff" stroke-width="2"/><path d="M10 5v5l3 2" fill="none" stroke="#fff" stroke-width="2" stroke-linecap="round"/></svg></span>
      <div><h3>TIME TO HIRE</h3><p>Combine local market coverage, with access to global markets to deliver exceptional people quickly.</p></div>
    </li>
    <li class="benefit">
      <span class="benefit-icon"><svg width="20" height="20" viewBox="0 0 20 20"><text x="3" y="14" font-family="Roboto,Arial,sans-serif" font-size="13" font-weight="700" fill="#fff">£</text><circle cx="14" cy="14" r="3" fill="none" stroke="#fff" stroke-width="1.5"/></svg></span>
      <div><h3>COST TO HIRE</h3><p>Reduce cost per hire by sharing the financial benefits of resourcing more efficiently together.</p></div>
    </li>
    <li class="benefit">
      <span class="benefit-icon"><svg width="20" height="20" viewBox="0 0 20 20"><circle cx="10" cy="10" r="8" fill="#fff"/><path d="M6 10l3 3 5-6" fill="none" stroke="#1ea7e1" stroke-width="2" stroke-linecap="round"/></svg></span>
      <div><h3>QUALITY OF HIRES</h3><p>Bring IT service delivery quality to the resourcing process to assure the quality of hires.</p></div>
    </li>
  </ul>
</section>

<section class="services" id="services">
  <h2 class="section-title">OUR SERVICES</h2>
  <div class="divider"><i></i><b></b><i></i></div>
  <p class="services-lead">Our focus is on saving you time and money on your IT resourcing, without compromising quality</p>
</section>

<div class="service-grid">
  <div class="badge" style="top:42px"><span class="b-name">vanq5</span><span class="b-role">RESOURCING</span></div>
  <div class="badge" style="top:170px"><span class="b-name">vanq5</span><span class="b-role">RESOURCING<br>MANAGEMENT</span></div>
  <div class="dotline" style="top:6px;height:128px"></div>
  <div class="dotline" style="top:142px;height:90px"></div>

  <div class="col-type" style="top:3px;height:41px">
    <svg width="24" height="24" viewBox="0 0 24 24"><circle cx="12" cy="12" r="10" fill="#fff" opacity=".9"/></svg>LOCAL</div>
  <div class="col-detail" style="top:3px;height:41px">High quality IT resources delivered on-site.<ul><li>Permanent or contract hires</li></ul></div>

  <div class="col-type" style="top:44px;height:92px">
    <svg width="30" height="30" viewBox="0 0 30 30"><circle cx="15" cy="15" r="13" fill="none" stroke="#fff" stroke-width="2"/><ellipse cx="15" cy="15" rx="6" ry="13" fill="none" stroke="#fff" stroke-width="1.5"/><path d="M2 15h26" stroke="#fff" stroke-width="1.5"/></svg>GLOBAL</div>
  <div class="col-detail" style="top:44px;height:92px">Access to global markets to deliver hard to find resources.<ul><li>High quality IT resourcing delivered from Eastern Europe.</li><li>Near-shoring – Permanent, flexible and project delivery solutions.</li><li>On-shoring – Bringing global resources to the UK</li></ul></div>

  <div class="col-type" style="top:136px;height:97px">
    <svg width="30" height="34" viewBox="0 0 30 34"><rect x="4" y="4" width="22" height="28" rx="2" fill="#fff"/><rect x="10" y="1" width="10" height="6" rx="1" fill="#cfe9f7"/><path d="M9 19l4 4 8-9" fill="none" stroke="#2fb34a" stroke-width="3" stroke-linecap="round"/></svg></div>
  <div class="col-detail" style="top:136px;height:97px">Take responsibility for some or all of your IT recruitment process.<ul><li>The greater responsibility, the lower the cost.</li><li>Maximize hiring cost and time savings from time to hire, lower churn, and improved candidate experience.</li><li>No service charge AND lower rates to reflect efficiencies.</li></ul></div>
</div>
</body>
</html>
```